I want a double sided flyer possibly with a picture of a lawn or grass.
Company name, phone number, email, and logo
Corvane Lawn Management, (404)672-8154,Corvane_Lawn@brisknet.com
Company services
Fertilization and weed control,Lawn and Landscape maintenance, mowing, pruning, aeration, landscape and Christmas lights,

```html
<!DOCTYPE html>
<html lang="en">
<head>
<meta charset="utf-8">
<title>Corvane Lawn Management – Flyer</title>
<link href="https://fonts.googleapis.com/css2?family=Ubuntu:wght@400;500;700&family=Open+Sans:wght@400;600&display=swap" rel="stylesheet">
<style>
  :root{
    --bg:#e9ebe6;
    --green:#1f8a3a;
    --green-dark:#0f6a2c;
    --green-light:#5fbf3a;
    --grass-1:#2f8f1c;
    --grass-2:#6cc23a;
    --grass-3:#3fa524;
    --white:#ffffff;
    --text:#6b6b6b;
  }
  *{box-sizing:border-box;margin:0;padding:0}
  html,body{width:1200px;height:707px;overflow:hidden;background:var(--bg)}
  .canvas{position:relative;width:1200px;height:707px}
  .flyer{position:absolute;top:50px;width:440px;height:607px;overflow:hidden;box-shadow:0 4px 14px rgba(0,0,0,.18)}

  /* Front side */
  .flyer--front{left:120px}
  .front__grass{position:absolute;inset:0;background:linear-gradient(180deg,var(--grass-2) 0%,var(--grass-3) 45%,var(--grass-1) 100%)}
  .front__band{position:absolute;top:0;bottom:0;left:100px;width:240px;background:rgba(255,255,255,.12)}
  .brand{position:absolute;top:80px;left:100px;width:240px;text-align:center;color:var(--white);font-family:'Ubuntu',sans-serif;font-weight:500;font-size:22px;line-height:1.25}
  .brand__mark{display:block;width:54px;height:54px;border-radius:50%;background:var(--white);margin:0 auto 14px}
  .front__contact{position:absolute;left:100px;right:0;bottom:70px;height:80px;background:rgba(0,0,0,.08);padding:12px 0 0 30px;color:var(--white);font-family:'Ubuntu',sans-serif}
  .front__phone{font-size:26px;font-weight:700;letter-spacing:.5px}
  .front__email{font-size:15px;font-weight:500;margin-top:6px}

  /* Back side */
  .flyer--back{left:640px;background:var(--white)}
  .back__shapes{position:absolute;inset:0}
  .back__title{position:absolute;top:10px;right:18px;text-align:right;color:var(--white);font-family:'Ubuntu',sans-serif;font-weight:700;font-size:19px;line-height:1.05}
  .service{position:absolute;width:128px;font-family:'Open Sans',sans-serif}
  .service__name{height:30px;display:flex;align-items:flex-end;color:var(--green);font-family:'Ubuntu',sans-serif;font-weight:700;font-size:11.5px;line-height:1.1}
  .service__photo{display:block;height:78px;margin-top:4px}
  .service__text{margin-top:8px;font-size:7.4px;line-height:1.3;color:var(--text);text-align:justify}
  .photo--spreader{background:linear-gradient(160deg,#cfe6b0,#3f8f2a)}
  .photo--garden{background:linear-gradient(160deg,#6fb34a,#c88aa0)}
  .photo--mower{background:linear-gradient(160deg,#5aa63a,#c0392b)}
  .photo--pruning{background:linear-gradient(160deg,#9bc37a,#3e6d2a)}
  .photo--aeration{background:linear-gradient(160deg,#4e9a2e,#8a6a45)}
  .photo--lights{background:radial-gradient(circle at 40% 50%,#e8b24a,#5a3a1a 70%,#2a1a0a)}
  .back__phone{position:absolute;left:20px;bottom:22px;color:var(--white);font-family:'Ubuntu',sans-serif;font-weight:700;font-size:22px}
  .back__brand{position:absolute;right:18px;bottom:22px;display:flex;align-items:center;gap:6px;color:var(--green);font-family:'Ubuntu',sans-serif;font-weight:500;font-size:11px;line-height:1.15}
  .back__brand-mark{flex:none;width:22px;height:22px;border-radius:50%;background:var(--green)}
</style>
</head>
<body>
<div class="canvas">

  <section class="flyer flyer--front">
    <div class="front__grass" role="img" aria-label="Photograph of a lush green lawn filling the page"></div>
    <div class="front__band"></div>
    <div class="brand">
      <span class="brand__mark"></span>
      Corvane<br>Lawn Management
    </div>
    <div class="front__contact">
      <p class="front__phone">(404)672-8154</p>
      <p class="front__email">Corvane_Lawn@brisknet.com</p>
    </div>
  </section>

  <section class="flyer flyer--back">
    <svg class="back__shapes" width="440" height="607" viewBox="0 0 440 607">
      <path d="M0 0H440V26C320 30 150 20 0 48Z" fill="#1f8a3a"/>
      <path d="M0 48C150 20 320 32 440 34" fill="none" stroke="#5fbf3a" stroke-width="3"/>
      <path d="M272 0H440V62H262Z" fill="#0f6a2c"/>
      <path d="M0 538C140 520 300 560 440 528V607H0Z" fill="#1f8a3a"/>
      <path d="M0 530C140 512 300 552 440 520" fill="none" stroke="#5fbf3a" stroke-width="3"/>
      <path d="M200 607C230 545 300 530 440 528V607Z" fill="#ffffff"/>
      <path d="M250 607C300 590 380 585 440 592V607Z" fill="#1f8a3a"/>
    </svg>
    <h2 class="back__title">COMPANY<br>SERVICES</h2>

    <article class="service" style="left:18px;top:62px">
      <h3 class="service__name">Fertilization and weed control</h3>
      <span class="service__photo photo--spreader" role="img" aria-label="Photo of a fertilizer spreader on a lawn"></span>
      <p class="service__text">Balanced feeding and targeted weed treatment keep turf thick, green and healthy through every season of the year.</p>
    </article>
    <article class="service" style="left:156px;top:62px">
      <h3 class="service__name">Lawn and Landscape maintenance</h3>
      <span class="service__photo photo--garden" role="img" aria-label="Photo of a tended garden bed with hostas and flowers"></span>
      <p class="service__text">Regular care for lawns, beds and borders, with edging, mulching and cleanup so your yard always looks its best.</p>
    </article>
    <article class="service" style="left:294px;top:62px">
      <h3 class="service__name">Mowing</h3>
      <span class="service__photo photo--mower" role="img" aria-label="Photo of a red lawn mower cutting grass"></span>
      <p class="service__text">Weekly mowing at the right height, with trimming and blowing of walks and drives included on every visit.</p>
    </article>

    <article class="service" style="left:18px;top:292px">
      <h3 class="service__name">Pruning</h3>
      <span class="service__photo photo--pruning" role="img" aria-label="Photo of pruning shears trimming a branch"></span>
      <p class="service__text">Careful shaping of shrubs, hedges and small trees to encourage strong growth and a neat, natural form.</p>
    </article>
    <article class="service" style="left:156px;top:292px">
      <h3 class="service__name">Aeration</h3>
      <span class="service__photo photo--aeration" role="img" aria-label="Photo of a soil core pulled from a lawn"></span>
      <p class="service__text">Core aeration loosens compacted soil so water, air and nutrients reach the roots and your lawn grows deeper.</p>
    </article>
    <article class="service" style="left:294px;top:292px">
      <h3 class="service__name">Landscape and Christmas lights</h3>
      <span class="service__photo photo--lights" role="img" aria-label="Photo of glowing string lights at night"></span>
      <p class="service__text">Outdoor lighting for paths and gardens, plus festive holiday light installation, removal and storage each winter.</p>
    </article>

    <p class="back__phone">(404)672-8154</p>
    <div class="back__brand" style="bottom:24px">
      <span class="back__brand-mark"></span>
      <span>Corvane<br>Lawn Management</span>
    </div>
  </section>

</div>
</body>
</html>
```